Digital Imaging Website Design Project

This project is for 3 page designs - The main Home page design, department page design & content page design which will utilize most of the home page components.

Client Background - http://www.kelrofab.com

An almost Forty year old established printing company that has a large client base of architect/engineering, as the print shop opened up as a blueprinting company, and over the years has grown, changed and expanded to offer document and digital file management for this industry. KRFab. has also always offered color printing services, but recently has expanded their color department to be able to offer amazing dimensional printing, and extreme cutting technology.

These new products and services will be targeted to new industries for repeatable printing needs, promotional, point of purchase color printing, as well as in-store, interior decor/wall. These new printing services are only offered by KRFAB in their area, and they want to convey that they are on the leading edge of color printing technology, while at the same time, not eliminating their existing primary business scaring away their traditional client base of architectural/engineering firms that use them for large format printing, scanning and document management services.

1 - Home Page Design
Primary Goals of the design:

1.Provide a new, eye catching engaging website that conveys the above expansion/growth/cutting edge company.
2.Full screen design please to move away from the 'center' bordered up website they currently have.
3.Design Components – We don't have any media to provide you with exception of our logo. We're looking for fresh design that is exciting and engaging imagery. Additionally, we are working on a color/effected version of our logo to place on the color division page, and this will probably tie in with the design you create for us.
4.It should be designed to be able to work as a responsive design as well so that when installed, will work across devices etc..
5.Colors – Same color scheme, but if you have an accent color you'd like to use to make the site pop, go for it!

Requirements:
1.The 4 divisions of the company should be the main feature so that the client depending on which department they are needing, will see those 4 choices clearly in the design, and they'll know to click on one of them to get more information and to their needed services.

2.The main goal of the site is to get visitors to place an order, there should be a feature on the home page for this call to action.

3.Put in an element that communicates the main benefit of KRFab. - an area for a 1-line Statement/Call to Action / Overall Company Benefit/

4.The 4 divisions need to have eye catching elements related to their products and services, and that clearly illustrate that the user should click on that to go to the appropriate area for products and services

Reprographics
This department is specifically geared to architect/engineering industry
BYLine for optional Use: Partnering with Building Industry Providers since 1975
Related pages for better understanding:
http://www.kelrofab.com/services/portland_professional_printing_services
http://www.kelrofab.com/services/reprographics
Digital File Management
This department is related to Architect/engineers, but can also apply to any other industry needing electronic document management, scanning, or archival services.
BYLine for optional use: Effective & Efficient Digital Solutions at every level.
Related Pages:
http://www.kelrofab.com/colorgraphics/electronic_file_document_management
http://www.kelrofab.com/colorgraphics/document_scanning_service
http://www.kelrofab.com/services/scanning_and_archiving

Color Graphics
This Department is newly expanded / has expanded services / they are focusing more of their efforts on this department and is a key reason for updated website design.
This Department image/representation should be stellar in the imagery to convey the excellence of the color department the services availble.
One of their newest products/services is dimensional printing – not 3-D, but raised element printing. Essentially a client could pick components on their graphic that that they want to 'bump' out, and additional layers would be put in place to create a popped out, dimensional effect. * Bonus points for creating the color department image that effectively conveys this new service – whether it's showing an abstract image/element that is actually raised off the page/paper/component. Additionally the color dimensional printing can be done on practically any material – glass, vinyl, material etc.... Please let me know if you have any questions on this.
BYLine for optional Use: See How Our Color Stands Out From the Rest
Related pages:
http://www.kelrofab.com/colorgraphics
http://www.kelrofab.com/colorgraphics/color_digital_imaging

Equipment & Supplies
This department provides specific supplies and hardware vs. printing products/services. Our largest client base is architects/engineers, but is not limited to this industry. Typical equipment is large printers, and supplies are typically paper products geared to the large format printing services, for the architect/engineers industry.
Byline for optional Use: In-House Printing & Fulfillment Services
Related pages:
http://www.kelrofab.com/varlen_tusk_equipment_sales
http://www.kelrofab.com/supplies

Additionally - Possibly have descriptive text sections below these 4 elements, but this is optional.

2.) Department/Division Page design -

This page should pull the home page element to over based on which division is selected.
Have a submenu design incorporated so that users can navigate to all the products and services that will be listed under that division
Contain a plugin design for FAQs – so that depending on which division page they are on, the appropriate FAQ's would display for use to have easy access to.
Contain a plugin design for – Contact Us easy form – short form –
Name
Company
Number
Email
Project Details/Questions: Text box

3.)Content Page design
This page should have main area for content
Area for an image with slideshow of other supporting images
Optional area for video – most (99%) of the pages will not have videos, but in the case we do, would like an area that will display videos effectively.
Optional FAQ plugin display
Contact plugin display

Global Elements:

Static and very visible site features that are in a position so that if user clicks beyond home page will still see these are:
Get a Quote
Place Order
Digital Plan-room
Call Today - 503-481-7962

Other global components:
SM Icons – QN, Chirpo, WorkLoop
Rotating Testimonial

Navigational Menu:
The KRF Difference
About
Sustainability
Products & Services
Reprograhics
Digital File Management
Color Graphics
Equipment & Supplies
Login
Blog
Contact Us

After the contest – What would be great to have is when a user clicks on one of the departments, it takes that visual element and continues onto it's department page for a smaller but related image - But this may be an after this web design contest.

Additionally will need some other design work on the interior pages, as well, so hoping to find a great designer to complete the other tasks – as well as be the go-to for future endeavors!

Thanks for looking at the project, and I look forward to any questions you may have.
Updates

Looking forward to hearing from interested designers! - If you're curious about my work, you can find my profile at:  https://www.gigmarla.com/users/~07b3e2f95d18c4a260

Target Market(s)

Please see description

Industry/Entity Type

Electronic

Requirements
Must have
• Please see description

```html
<!DOCTYPE html>
<html lang="en">
<head>
<meta charset="utf-8">
<title>KRF Digital Imaging</title>
<link href="https://fonts.googleapis.com/css2?family=Figtree:wght@300;400;600;800&display=swap" rel="stylesheet">
<style>
:root{
  --brand:#1a1a8c;
  --brand-deep:#16169a;
  --text:#555;
  --muted:#777;
  --band:#f4f4f4;
  --line:#dcdcdc;
  --footer:#333;
  --footer-text:#5c5c5c;
  --footer-light:#bbb;
  --social:#666;
}
*{margin:0;padding:0;box-sizing:border-box}
html,body{width:1200px;height:1153px;overflow:hidden;background:#fff;font-family:'Figtree',sans-serif;color:var(--text)}
.site{position:relative;width:1200px;height:1153px}
a{color:inherit;text-decoration:none}

/* header */
.header{position:absolute;left:0;top:0;width:1200px;height:181px;background:#fff}
.brand{position:absolute;left:45px;top:58px;display:flex;align-items:center;gap:14px}
.brand-mark{width:64px;height:64px;border-radius:50%;background:var(--brand)}
.brand-name{font-weight:600;font-size:17px;line-height:20px;color:var(--brand);text-transform:uppercase;letter-spacing:.3px}
.rule-v{position:absolute;top:53px;width:1px;height:76px;background:var(--line)}
.nav{position:absolute;top:0;left:0}
.nav a{position:absolute;font-size:16px;font-weight:300;color:#555;white-space:nowrap;transform:translateY(-50%)}
.nav a.active{color:var(--brand);font-weight:400}
.social{position:absolute;left:948px;top:52px;display:flex;gap:9.5px}
.social span{width:32px;height:32px;border-radius:50%;background:var(--social);display:block}
.call{position:absolute;left:948px;top:100px;display:flex;align-items:center;gap:14px;font-size:30px;font-weight:300;color:#777;letter-spacing:-.5px}

/* band */
.band{position:absolute;left:0;top:181px;width:1200px;height:887px;background:var(--band)}
.tagline{position:absolute;left:45px;top:29px;font-size:37px;font-weight:300;color:var(--brand);letter-spacing:-1px;text-transform:uppercase}
.divisions{position:absolute;left:0;top:98px;width:1200px;height:300px;display:flex}
.division{position:relative;width:300px;height:300px;overflow:hidden}
.division .caption{position:absolute;left:0;bottom:0;width:100%;height:67px;background:rgba(20,20,20,.6);color:#fff;font-size:26px;font-weight:300;padding-left:19px;line-height:67px;letter-spacing:-.3px}
.d-repro{background:linear-gradient(160deg,#2f5f8c 0%,#9fb6c4 40%,#e2e6e0 70%,#8aa06f 100%)}
.d-color{background:linear-gradient(135deg,#e8eef2 0%,#2bb0d8 25%,#ec3a8c 50%,#f26b1d 70%,#f5d020 100%)}
.d-equip{background:linear-gradient(120deg,#d8b24a 0%,#8a7a4e 35%,#1e2448 65%,#4a4a4a 100%)}
.d-digital{background:var(--brand-deep);color:#fff;padding:28px 18px 0 18px}
.d-digital h2{font-size:43px;font-weight:800;line-height:45px;letter-spacing:-1.2px}
.d-digital p{margin-top:16px;font-size:13px;line-height:17px;font-weight:300;letter-spacing:.3px}
.d-digital .more{display:block;margin-top:18px;font-size:19px;letter-spacing:1.5px;font-weight:400}

.welcome{position:absolute;left:45px;top:462px;width:1110px}
.welcome h1{font-size:28px;font-weight:300;color:var(--brand);letter-spacing:-.8px;text-transform:uppercase}
.welcome p{margin-top:21px;margin-left:2px;font-size:19.5px;line-height:24.4px;font-weight:300;letter-spacing:1.3px;color:#666}

.actions{position:absolute;left:46px;top:652px;width:1107px;height:189px;border-top:1px solid var(--line);border-bottom:1px solid var(--line);display:flex}
.action{width:277px;height:100%;border-right:1px solid var(--line);text-align:center;padding-top:40px}
.action:nth-child(3){width:276px}
.action svg{display:block;margin:0 auto;height:60px}
.action span{display:block;margin-top:27px;font-size:22px;font-weight:400;color:#333;letter-spacing:-.8px}
.testimonial{flex:1;padding:25px 0 0 24px}
.testimonial h3{font-size:22px;font-weight:800;color:var(--brand);letter-spacing:-.8px}
.testimonial p{margin-top:10px;font-size:15.5px;line-height:20px;font-weight:300;letter-spacing:.6px;color:#666}
.testimonial cite{display:block;margin-top:12px;font-style:normal;font-weight:600;font-size:16px;color:var(--brand);letter-spacing:.5px}

/* footer */
.footer{position:absolute;left:0;top:1068px;width:1200px;height:85px;background:var(--footer)}
.copy{position:absolute;left:44px;top:41px;transform:translateY(-50%);font-size:16px;font-weight:300;color:var(--footer-text);letter-spacing:.8px}
.contact{position:absolute;top:41px;transform:translateY(-50%);display:flex;align-items:center;gap:13px;font-size:16px;font-weight:300;color:var(--footer-light);letter-spacing:.5px}
</style>
</head>
<body>
<div class="site">
  <header class="header">
    <a class="brand" href="#">
      <span class="brand-mark"></span>
      <span class="brand-name">Kelro Fabrication<br>Company, Inc.</span>
    </a>
    <span class="rule-v" style="left:384px"></span>
    <nav class="nav">
      <a class="active" href="#" style="left:423px;top:67px">HOME</a>
      <a href="#" style="left:424px;top:95px">SERVICES</a>
      <a href="#" style="left:423px;top:123px">COLOR GRAPHICS</a>
      <a href="#" style="left:606px;top:65px">EQUIPMENT SALES</a>
      <a href="#" style="left:607px;top:95px">SUPPLIES</a>
      <a href="#" style="left:607px;top:123px">ABOUT US</a>
      <a href="#" style="left:794px;top:65px">CONTACT</a>
    </nav>
    <span class="rule-v" style="left:911px"></span>
    <div class="social" aria-label="Social links">
      <span aria-label="QN"></span><span aria-label="Chirpo"></span><span aria-label="WorkLoop"></span><span aria-label="Circlet"></span>
    </div>
    <div class="call">
      <svg width="14" height="28" viewBox="0 0 14 28" aria-hidden="true"><path d="M11 2 L6 2 Q1 2 1 8 L1 20 Q1 26 6 26 L11 26 L11 21 L7 21 L7 7 L11 7 Z" fill="#1a1a8c"/></svg>
      <span>(503) 481-7962</span>
    </div>
  </header>

  <main class="band">
    <h2 class="tagline">Color Services for Designers and Marketers</h2>

    <section class="divisions">
      <a class="division d-repro" href="#" role="img" aria-label="Photo of a large format printer feeding out a printed map">
        <span class="caption">Reprographics</span>
      </a>
      <a class="division d-digital" href="#">
        <h2>Digital File Management</h2>
        <p>Lorem ipsum dolor sit amet, consectetuer adipiscing elit, sed diam nonummy nibh euismod tincidunt ut laoreet dolore magna aliquam erat volutpat. Ut wisi enim ad minim veniam, quis nostrud exerci tation.</p>
        <span class="more">LEARN MORE</span>
      </a>
      <a class="division d-color" href="#" role="img" aria-label="Photo of a fanned-out colour swatch guide">
        <span class="caption">Color Graphics</span>
      </a>
      <a class="division d-equip" href="#" role="img" aria-label="Photo of open ink cans in yellow and dark blue">
        <span class="caption">Equipment &amp; Supplies</span>
      </a>
    </section>

    <section class="welcome">
      <h1>Welcome to KRF Digital Imaging</h1>
      <p>Kelro Fabrication (KRF) is a full service reprographics company serving Oregon and Southwest Washington’s design and building community. We utilize the latest digital technologies to provide a wide range of reprographics and graphic imaging services.</p>
    </section>

    <section class="actions">
      <a class="action" href="#">
        <svg viewBox="0 0 64 64" width="64" aria-hidden="true">
          <rect x="2" y="4" width="60" height="40" rx="2" fill="#1a1a8c"/>
          <rect x="10" y="12" width="34" height="4" fill="#fff"/>
          <rect x="10" y="20" width="26" height="4" fill="#fff"/>
          <rect x="10" y="28" width="18" height="4" fill="#fff"/>
          <path d="M52 18 L58 24 L30 56 L20 60 L24 50 Z" fill="#1a1a8c" stroke="#fff" stroke-width="2"/>
        </svg>
        <span>GET A QUOTE</span>
      </a>
      <a class="action" href="#">
        <svg viewBox="0 0 64 64" width="64" aria-hidden="true">
          <path d="M2 6 L12 6 L20 42 L54 42" fill="none" stroke="#1a1a8c" stroke-width="5" stroke-linejoin="round"/>
          <path d="M14 14 L60 14 L54 36 L19 36 Z" fill="#1a1a8c"/>
          <path d="M24 20 H54 M22 28 H52 M30 16 V34 M40 16 V34 M48 16 V34" stroke="#fff" stroke-width="2"/>
          <circle cx="24" cy="54" r="5" fill="#1a1a8c"/><circle cx="48" cy="54" r="5" fill="#1a1a8c"/>
        </svg>
        <span>PLACE ORDER</span>
      </a>
      <a class="action" href="#">
        <svg viewBox="0 0 64 64" width="64" aria-hidden="true">
          <path d="M32 4 A28 26 0 1 1 18 52 L6 60 L10 46 A28 26 0 0 1 32 4 Z" fill="#1a1a8c"/>
          <path d="M32 10 A22 20 0 1 1 19 46 L13 50 L15 42 A22 20 0 0 1 32 10 Z" fill="#fff"/>
          <rect x="20" y="26" width="7" height="14" rx="2" fill="#1a1a8c"/>
          <rect x="29" y="20" width="7" height="20" rx="2" fill="#1a1a8c"/>
          <rect x="38" y="24" width="7" height="16" rx="2" fill="#1a1a8c"/>
        </svg>
        <span>DIGITAL PLAN-ROOM</span>
      </a>
      <div class="testimonial">
        <h3>TESTIMONIALS</h3>
        <p>“Lorem ipsum dolor sit amet, consectetuer adipiscing elit, sed diam nonummy nibh euismod.”</p>
        <cite>Dana Merrow</cite>
      </div>
    </section>
  </main>

  <footer class="footer">
    <p class="copy">Copyright 2013 Kelro Fabrication Inc.</p>
    <div class="contact" style="left:806px">
      <svg width="16" height="26" viewBox="0 0 16 26" aria-hidden="true"><rect x="1" y="1" width="14" height="24" rx="2" fill="none" stroke="#999" stroke-width="2"/><circle cx="8" cy="21" r="1.5" fill="#999"/></svg>
      <span>(503) 481-7962</span>
    </div>
    <div class="contact" style="left:984px">
      <svg width="24" height="17" viewBox="0 0 24 17" aria-hidden="true"><rect x="0" y="0" width="24" height="17" fill="#888"/><path d="M0 0 L12 9 L24 0" fill="none" stroke="#555" stroke-width="1.5"/></svg>
      <span>info@kelrofab.com</span>
    </div>
  </footer>
</div>
</body>
</html>
```